Real Estate Virtual 360 Tour Web Home Page [Design Only]

see new upload mockup attached

We want new design ideas for our home page.

Link to video from web dev team of wireframe for reference: https://files.quorvantshare.net/d/7q-WpR2n8Lx4Tb6Hc0Yv9Ke3Mz5Ud/view?usp=sharing

Things desired on the home page:

Book a shoot now - Multiple markets,links to the corresponding market page for actual booking

1 Complete Package - includes Video, 3D Doviquell Tours, Exterior 360 Tours, Map, Agent Profile, Floor Plans, 2D Photos with blue sky and twilight sky guarantee

How it Works-https://clipnestra.net/582716049

Pricing-https://brisklumehomes.net/pricing/

House Search-https://brisklumehomes.net/

Footer
Updates

Target Market(s)

Real Estate Agents, Realtors, Home Buyers

Number of Pages Required

1 page

Font styles to use
Sans Serif

Colors
0555a3

Requirements
Must have
• see new upload mockup attached

Footer

```html
<!DOCTYPE html>
<html lang="en">
<head>
<meta charset="utf-8">
<title>Brisklume Homes – Marketing Media for Real Estate</title>
<link href="https://fonts.googleapis.com/css2?family=Lato:wght@300;400;700;900&family=Merriweather:wght@700&display=swap" rel="stylesheet">
<style>
:root{
  --brand:#0555a3;
  --brand-dark:#04447f;
  --tile:#dbe8f7;
  --tile-deep:#c9dcf2;
  --ink:#222;
  --muted:#8a8a8a;
  --soft:#f3f3f3;
  --topbar:#858585;
  --footer:#2b2b2b;
  --star:#f5c518;
}
*{box-sizing:border-box;margin:0;padding:0}
html,body{width:1200px;height:4167px;overflow:hidden}
body{position:relative;font-family:'Lato',sans-serif;color:var(--ink);background:#fff}
.abs{position:absolute}
.serif{font-family:'Merriweather',serif;font-weight:700}
.btn{position:absolute;display:flex;align-items:center;justify-content:center;font-size:12px;font-weight:700;text-transform:uppercase;border-radius:4px;letter-spacing:.2px}
.btn-solid{background:var(--brand);color:#fff}
.btn-line{border:2px solid var(--brand);color:var(--brand);background:#fff}
.soc{display:inline-block;width:14px;height:14px;background:#fff;border-radius:2px;margin-left:12px}

/* top bar & nav */
.topbar{left:0;top:0;width:1200px;height:32px;background:var(--topbar);color:#fff;font-size:13px}
.topbar span{position:absolute;top:8px}
.nav{left:0;top:32px;width:1200px;height:73px;background:#fff;box-shadow:0 2px 6px rgba(0,0,0,.06)}
.logo{position:absolute;font-weight:900;font-size:20px;color:var(--brand);letter-spacing:.5px;line-height:1.05}
.nav a{position:absolute;top:29px;font-size:13px;color:#333;text-decoration:none;text-transform:uppercase}
.nav .cta{left:899px;top:0;width:181px;height:73px;background:var(--brand);color:#fff;display:flex;align-items:center;justify-content:center;font-size:13px}

/* hero */
.hero-photo{left:0;top:105px;width:1200px;height:569px;background:linear-gradient(180deg,#c7d9ea 0%,#a8b4b8 40%,#5e6f4f 72%,#3f6a2a 100%)}
.hero-card{left:580px;top:213px;width:502px;height:330px;background:#fff;box-shadow:0 4px 18px rgba(0,0,0,.12)}
.hero-card .kicker{position:absolute;left:66px;top:48px;font-family:'Merriweather',serif;font-size:14px;color:var(--brand);text-transform:uppercase}
.hero-card h1{position:absolute;left:66px;top:82px;font-size:31px;line-height:44px;color:#111}
.hero-card p{position:absolute;left:66px;top:180px;font-size:14px;line-height:22px;color:#555;width:380px}
.arrow-box{position:absolute;width:50px;height:50px;background:#fff;display:flex;align-items:center;justify-content:center}
.dots{position:absolute;display:flex;gap:9px;align-items:center}
.dots i{display:block;width:8px;height:8px;border-radius:50%;background:#fff}
.dots i.on{width:24px;border-radius:4px}
.dots.blue i{background:var(--brand)}

/* offer */
.offer-title{right:778px;top:742px;font-size:38px;text-align:right}
.offer-text{right:778px;top:822px;width:300px;font-size:14px;line-height:22.6px;color:var(--muted);text-align:right;font-weight:300}
.tile{position:absolute;width:238px;height:175px;background:var(--tile);display:flex;flex-direction:column;align-items:center;justify-content:flex-start;padding-top:42px;color:var(--brand);font-size:14px;text-align:center;line-height:18px}
.tile svg{height:56px;margin-bottom:16px}

/* clients / how it works */
.band{left:0;top:1205px;width:1200px;height:771px;background:var(--soft)}
.sec-title{font-size:33px}
.review{left:119px;top:1376px;width:333px;height:496px;background:var(--tile)}
.review .foot{position:absolute;left:0;bottom:0;width:333px;height:89px;background:var(--tile-deep)}
.review p{position:absolute;left:36px;top:125px;width:262px;text-align:center;font-size:14px;line-height:22.5px;color:var(--muted);font-weight:300}
.sq{position:absolute;width:41px;height:40px;background:#8d8d8d;color:#fff;display:flex;align-items:center;justify-content:center}
.step-n{position:absolute;left:585px;width:60px;height:60px;background:var(--brand);color:#fff;font-size:20px;display:flex;align-items:center;justify-content:center}
.step-t{position:absolute;left:661px;width:420px;font-size:14px;line-height:22px;color:#222}

/* package */
.pack-title{left:119px;top:2030px;font-size:33px;line-height:45px}
.video{left:476px;top:1979px;width:724px;height:409px;background:linear-gradient(160deg,#22324c 0%,#3a3a36 55%,#8a6b3c 100%)}

/* pricing */
.price-panel{left:446px;top:2599px;width:754px;height:517px;background:var(--tile)}
.ptab{position:absolute;left:120px;font-size:17px;text-transform:uppercase;color:#222;line-height:22px}
.ptab small{display:block;text-transform:none;font-size:16px;color:#555}
.prow{position:absolute;left:510px;width:568px;background:#fff}
.prow .tag{position:absolute;left:0;top:0;width:90px;height:100%;background:var(--brand);color:#fff;padding:10px 0 0 24px;font-size:11px;line-height:13px}
.prow .tag b{display:block;font-size:19px;line-height:24px}
.prow .lbl{position:absolute;left:111px;top:20px;font-size:14px;color:#222}
.chev{position:absolute;right:28px;top:22px}

/* team */
.ph{position:absolute;width:225px;background:linear-gradient(160deg,#b9b1a6,#5b554f)}
.team-title{right:122px;top:3235px;font-size:38px}
.team-text{right:122px;top:3302px;width:320px;text-align:right;font-size:14px;line-height:22.5px;color:var(--muted);font-weight:300}

/* newsletter & footer */
.footer{left:0;top:3824px;width:1200px;height:343px;background:var(--footer)}
.news{left:163px;top:3768px;width:875px;height:108px;background:var(--brand);border-left:10px solid var(--brand-dark);border-right:10px solid var(--brand-dark)}
.fcol{position:absolute;color:#ddd;font-size:13px;line-height:30px}
.fcol h4{font-size:15px;font-weight:400;color:#fff;margin-bottom:12px}
</style>
</head>
<body>

<!-- top bar -->
<div class="abs topbar">
  <svg class="abs" style="left:128px;top:9px" width="14" height="14" viewBox="0 0 24 24" fill="none" stroke="#fff" stroke-width="2"><path d="M5 3h4l2 5-3 2a12 12 0 0 0 6 6l2-3 5 2v4a2 2 0 0 1-2 2A18 18 0 0 1 3 5a2 2 0 0 1 2-2z"/></svg>
  <span style="left:152px">720-555-0148</span>
  <svg class="abs" style="left:264px;top:10px" width="16" height="12" viewBox="0 0 16 12" fill="none" stroke="#fff" stroke-width="1.4"><rect x="1" y="1" width="14" height="10"/><path d="M1 1l7 6 7-6"/></svg>
  <span style="left:288px">hello@brisklumehomes.net</span>
  <div class="abs" style="left:931px;top:9px"><i class="soc"></i><i class="soc"></i><i class="soc"></i><i class="soc"></i></div>
</div>

<!-- nav -->
<nav class="abs nav">
  <div class="logo" style="left:124px;top:16px">BRISKLUME<br>HOMES</div>
  <a style="left:303px">Home</a>
  <a style="left:370px">Properties</a>
  <a style="left:474px">Solutions</a>
  <a style="left:575px">Gallery</a>
  <a style="left:657px">Pricing</a>
  <a style="left:736px">Career</a>
  <a style="left:812px">Contact</a>
  <a class="cta">Schedule a Shoot</a>
</nav>

<!-- hero -->
<div class="abs hero-photo" role="img" aria-label="Photo of a shingled two-storey house with a white porch, lawn and trees"></div>
<div class="arrow-box" style="left:30px;top:358px"><svg width="10" height="14" viewBox="0 0 10 14"><path d="M8 1L2 7l6 6" fill="none" stroke="#333" stroke-width="2"/></svg></div>
<div class="arrow-box" style="left:1117px;top:358px"><svg width="10" height="14" viewBox="0 0 10 14"><path d="M2 1l6 6-6 6" fill="none" stroke="#333" stroke-width="2"/></svg></div>
<div class="abs hero-card">
  <div class="kicker">Welcome to Brisklume Homes</div>
  <h1 class="serif">The Best Marketing Media<br>for Real Estate</h1>
  <p>Lorem ipsum dolor sit amet, consectetur adipiscing elit. Nullam iaculis interdum dui eget tempus.</p>
  <div class="btn btn-line" style="left:66px;top:248px;width:132px;height:37px;border-color:#666;color:#333">Learn More</div>
  <div class="btn btn-solid" style="left:204px;top:248px;width:175px;height:37px">Search Houses</div>
</div>
<div class="dots" style="left:553px;top:624px"><i></i><i class="on"></i><i></i><i></i><i></i></div>

<!-- what we offer -->
<h2 class="abs serif offer-title">What we offer</h2>
<p class="abs offer-text">Lorem ipsum dolor sit amet, consectetur adipiscing elit. Cras est magna, consectetur ut metus vel, porta posuere maurist. Curabitur congue risus sem, in gravida leo molestie quis. Duis hendrerit, enim id efficitur rutrum, ipsum sapien gravida est, non placerat mi purus a velit. Quisque rutrum diam in libero laoreet malesuada. Etiam tincidunt auctor leo sit amet varius. Pellentesque eu metus magna. Aliquam semper tempus massa, sit amet lobortis urna pharetra in. Morbi non diam et diam.</p>
<div class="btn btn-solid" style="left:143px;top:1105px;width:130px;height:37px">Learn More</div>
<svg class="abs" style="left:293px;top:1107px" width="32" height="32" viewBox="0 0 32 32"><circle cx="16" cy="16" r="14.5" fill="none" stroke="#333" stroke-width="1.5"/><path d="M13 10l9 6-9 6z" fill="#333"/></svg>
<div class="abs" style="left:335px;top:1116px;font-size:12px;font-weight:700;color:#333">WATCH INTRO</div>

<div class="tile" style="left:481px;top:675px"><svg viewBox="0 0 64 50" width="72" fill="none" stroke="#0555a3" stroke-width="2"><path d="M4 8h20M40 8h20M14 8v8M50 8v8M14 16h36M22 16l4 14h12l4-14"/><circle cx="32" cy="36" r="5"/><path d="M24 30l-6 12M40 30l6 12"/></svg>90 Sec Drone Shoot</div>
<div class="tile" style="left:722px;top:675px"><svg viewBox="0 0 64 56" width="64" fill="none" stroke="#0555a3" stroke-width="2"><path d="M32 4v10M32 14l-18 9v20l18 9 18-9V23zM14 23l18 9 18-9M32 32v20"/><path d="M28 8l4-4 4 4"/></svg>Doviquell 3D Virtual Tour</div>
<div class="tile" style="left:963px;top:675px"><svg viewBox="0 0 64 50" width="66" fill="none" stroke="#0555a3" stroke-width="2"><path d="M6 6h52v38H6zM6 22h16v22M22 6v10M36 6v16h22M36 30v14M36 30h10"/></svg>CAD Schematic Floor Plans</div>
<div class="tile" style="left:481px;top:853px"><svg viewBox="0 0 64 50" width="64" fill="none" stroke="#0555a3" stroke-width="2"><path d="M6 14h12l4-6h18l4 6h12v26H6z"/><circle cx="34" cy="26" r="9"/><text x="40" y="48" font-size="11" fill="#0555a3" stroke="none" font-family="Lato,sans-serif" font-weight="900">HDR</text></svg>HDR Still Photography</div>
<div class="tile" style="left:722px;top:853px"><svg viewBox="0 0 64 50" width="66" fill="none" stroke="#0555a3" stroke-width="2"><circle cx="42" cy="16" r="7"/><path d="M42 2v4M54 16h4M51 7l3-3M33 7l-3-3M12 42h34a9 9 0 0 0 0-18 13 13 0 0 0-25 3 8 8 0 0 0-9 15z"/></svg>Blue Sky &amp; Twilight Sky<br>Guarantee</div>
<div class="tile" style="left:963px;top:853px"><svg viewBox="0 0 64 50" width="64" fill="none" stroke="#0555a3" stroke-width="2"><rect x="6" y="4" width="52" height="42"/><path d="M6 12h52M12 20h16v18H12zM34 22h18M34 30h18M34 38h12"/></svg>Eye Catching Landing Page</div>
<div class="tile" style="left:481px;top:1031px"><svg viewBox="0 0 64 56" width="62" fill="none" stroke="#0555a3" stroke-width="2"><path d="M32 4a10 10 0 0 1 10 10c0 9-10 20-10 20S22 23 22 14A10 10 0 0 1 32 4z"/><circle cx="32" cy="14" r="4"/><path d="M20 32l-12 18h48L44 32M16 50l14-12M48 50L36 40"/></svg>Location On Map With<br>Landmarks</div>
<div class="tile" style="left:722px;top:1031px"><svg viewBox="0 0 64 56" width="64" fill="none" stroke="#0555a3" stroke-width="2"><rect x="8" y="4" width="48" height="36"/><circle cx="32" cy="18" r="6"/><path d="M22 36c0-7 4-10 10-10s10 3 10 10M4 44h56M24 52h16"/></svg>Agent Profile</div>
<div class="tile" style="left:963px;top:1031px"><svg viewBox="0 0 64 50" width="66" fill="none" stroke="#0555a3" stroke-width="2"><path d="M4 6c18 6 38 6 56 0v38c-18-6-38-6-56 0z"/><circle cx="44" cy="16" r="4"/><path d="M8 38l14-16 12 12 8-6 14 10"/></svg>Exterior 360 Panoramas In 4K</div>

<!-- clients / how it works -->
<div class="abs band"></div>
<h2 class="abs serif sec-title" style="left:127px;top:1290px">What our clients say</h2>
<div class="sq" style="left:66px;top:1588px"><svg width="8" height="12" viewBox="0 0 8 12"><path d="M7 1L2 6l5 5" fill="none" stroke="#fff" stroke-width="1.6"/></svg></div>
<div class="sq" style="left:466px;top:1588px"><svg width="8" height="12" viewBox="0 0 8 12"><path d="M1 1l5 5-5 5" fill="none" stroke="#fff" stroke-width="1.6"/></svg></div>
<div class="abs review">
  <svg class="abs" style="left:114px;top:30px" width="106" height="20" viewBox="0 0 106 20"><g fill="#f5c518"><path id="st" d="M10 1l2.6 6 6.4.6-4.9 4.3 1.5 6.3L10 15l-5.6 3.2 1.5-6.3L1 7.6 7.4 7z"/><use href="#st" x="21"/><use href="#st" x="42"/><use href="#st" x="63"/><use href="#st" x="84"/></g></svg>
  <div class="abs" style="left:0;top:72px;width:333px;text-align:center;font-size:22px;font-weight:700">Exceptional service</div>
  <p>Lorem ipsum dolor sit amet, consectetur adipiscing elit. Cras est magna, consectetur ut metus vel, porta posuere maurist. Curabitur congue risus sem, in gravida leo molestie quis. Duis hendrerit, enim id efficitur rutrum, ipsum sapien gravida est, non placerat mi purus a velit. Quisque rutrum diam in libero laoreet malesuada. Etiam tincidunt auctor leo sit amet varius. Pellentesque eu metus magna. urna pharetra in. Morbi non diam et diam.</p>
  <div class="foot">
    <div class="abs" role="img" aria-label="Client portrait" style="left:64px;top:12px;width:64px;height:64px;border-radius:50%;background:linear-gradient(160deg,#d8d4cf,#6d6660)"></div>
    <div class="abs" style="left:153px;top:28px;font-size:15px;font-weight:700">Miles T. Varden</div>
    <div class="abs" style="left:153px;top:50px;font-size:12px;color:#555">31<sup>st</sup> Nov 2021</div>
  </div>
</div>
<div class="dots blue" style="left:238px;top:1902px"><i></i><i class="on"></i><i></i><i></i><i></i></div>

<h2 class="abs serif sec-title" style="right:122px;top:1290px">How it works</h2>
<p class="abs" style="left:603px;top:1350px;width:484px;text-align:center;font-size:14px;line-height:22.5px;color:#555;font-weight:300">Lorem ipsum dolor sit amet, consectetur adipiscing elit. Cras est magna, consectetur ut metus vel, porta posuere mauris. Curabitur congue risus sem, in gravida leo molestie quis. Duis hendrerit, enim id efficitur rutrum.</p>
<div class="step-n" style="top:1450px">01</div><div class="step-t" style="top:1469px">Lorem ipsum dolor sit amet, consectetur adipiscing elit. Cras est.</div>
<div class="step-n" style="top:1516px">02</div><div class="step-t" style="top:1524px">Lorem ipsum dolor sit amet, consectetur adipiscing elit. Cras est magna, consectetur ut metus vel, porta posuere mauris.</div>
<div class="step-n" style="top:1591px">03</div><div class="step-t" style="top:1599px">Lorem ipsum dolor sit amet, consectetur adipiscing elit. Cras est magna, consectetur.</div>
<div class="step-n" style="top:1666px">04</div><div class="step-t" style="top:1694px;transform:translateY(-10px)">Lorem ipsum dolor sit amet, consectetur adipiscing elit.</div>
<div class="btn btn-solid" style="left:946px;top:1778px;width:132px;height:37px">Learn More</div>

<!-- complete package -->
<h2 class="abs serif pack-title">Single COMPLETE<br>PACKAGE for all<br>your digital<br>marketing needs!</h2>
<p class="abs" style="left:121px;top:2228px;width:300px;font-size:17px;line-height:22px;color:var(--muted);font-weight:300">Watch detailed explanation on our newest package that covers all your digital marketing needs.</p>
<div class="btn btn-solid" style="left:119px;top:2320px;width:175px;height:37px">Schedule a Shoot</div>
<div class="abs video" role="img" aria-label="Video still of a modern house lit at twilight"></div>
<svg class="abs" style="left:786px;top:2128px" width="104" height="104" viewBox="0 0 104 104"><circle cx="52" cy="52" r="49" fill="rgba(255,255,255,.12)" stroke="#fff" stroke-width="3"/><path d="M42 32l32 20-32 20z" fill="#fff"/></svg>

<!-- pricing -->
<h2 class="abs serif" style="left:0;top:2448px;width:1200px;text-align:center;font-size:33px">Find A Package That’s Right For You</h2>
<p class="abs" style="left:200px;top:2514px;width:800px;text-align:center;font-size:14px;line-height:20px;color:#555;font-weight:300">Lorem ipsum dolor sit amet, consectetur adipiscing elit. Cras est magna, consectetur ut metus vel, porta posuere maurist. Curabitur congue risus sem, in gravida leo molestie quis. Duis hendrerit, enim id efficitur rutrum.</p>
<div class="abs price-panel"></div>
<div class="abs" style="left:66px;top:2655px;width:380px;height:76px;background:#fff;border-left:3px solid var(--brand);border-bottom:1px solid #d6d6d6"></div>
<div class="ptab" style="top:2670px">Brisklume Tour Shoot<small>(Front range colorado)</small></div>
<div class="ptab" style="top:2745px">Land Package<small>(Front range colorado)</small></div>
<div class="ptab" style="top:2820px">Commercial Properties<small>(Lodging, Hotel, Office over 10,000ft²)</small></div>
<div class="ptab" style="top:2895px">Big Box Commercial</div>

<div class="prow" style="top:2648px;height:55px"><div class="tag">3 Hours<b>$249</b></div><div class="lbl">1100ft² or less Condo FULL PACKAGE</div><svg class="chev" width="12" height="8"><path d="M1 1l5 5 5-5" fill="none" stroke="#333" stroke-width="1.5"/></svg></div>
<div class="prow" style="top:2717px;height:145px"><div class="tag" style="padding-top:52px">3 Hours<b>$299</b></div><div class="lbl">1101 - 2700ft²&nbsp; House FULL PACKAGE</div>
  <div class="abs" style="left:111px;top:46px;width:400px;font-size:13px;line-height:17px;color:var(--muted)">*acreage on houses are an additional $100 per 25 acre block and is applied after 1 acre</div>
  <div class="btn btn-line" style="left:358px;top:89px;width:148px;height:30px;font-size:10px;border-width:1.5px;border-radius:5px">Book This Service</div>
  <svg class="chev" width="12" height="8"><path d="M1 7l5-5 5 5" fill="none" stroke="#333" stroke-width="1.5"/></svg></div>
<div class="prow" style="top:2867px;height:55px"><div class="tag">4 Hours<b>$399</b></div><div class="lbl">2700 - 4200ft² House FULL PACKAGE</div><svg class="chev" width="12" height="8"><path d="M1 1l5 5 5-5" fill="none" stroke="#333" stroke-width="1.5"/></svg></div>
<div class="prow" style="top:2937px;height:55px"><div class="tag">5 Hours<b>$549</b></div><div class="lbl">4200 - 7200ft² House FULL PACKAGE</div><svg class="chev" width="12" height="8"><path d="M1 1l5 5 5-5" fill="none" stroke="#333" stroke-width="1.5"/></svg></div>
<div class="prow" style="top:3006px;height:55px"><div class="tag">6 Hours<b>$699</b></div><div class="lbl">7200 - 9900ft² House FULL PACKAGE</div><svg class="chev" width="12" height="8"><path d="M1 1l5 5 5-5" fill="none" stroke="#333" stroke-width="1.5"/></svg></div>

<!-- team -->
<div class="ph" role="img" aria-label="Team member portrait" style="left:0;top:3187px;height:225px;background:linear-gradient(160deg,#c8ccd0,#3a3d42)"></div>
<div class="ph" role="img" aria-label="Team member portrait" style="left:233px;top:3187px;height:225px;background:linear-gradient(160deg,#b87a58,#2a2a2e)"></div>
<div class="ph" role="img" aria-label="Co-founder portrait with blue overlay" style="left:465px;top:3187px;height:225px;background:linear-gradient(160deg,#5d7fb0,#3a5a8e)">
  <div class="abs" style="left:56px;top:98px"><i class="soc" style="margin:0 8px 0 0"></i><i class="soc" style="margin:0 8px 0 0"></i><i class="soc" style="margin:0 8px 0 0"></i><i class="soc" style="margin:0"></i></div>
  <div class="abs" style="left:0;top:120px;width:225px;text-align:center;color:#fff;font-size:14px;font-weight:700">Elena R. Marsh<br><span style="font-weight:300">Co-founder</span></div>
</div>
<div class="ph" role="img" aria-label="Team member working at a laptop" style="left:0;top:3420px;height:226px;background:linear-gradient(160deg,#d5d6d8,#2e3440)"></div>
<div class="ph" role="img" aria-label="Team member portrait" style="left:233px;top:3420px;height:226px;background:linear-gradient(160deg,#4a4a4a,#141414)"></div>
<div class="ph" role="img" aria-label="Team member portrait outdoors" style="left:465px;top:3420px;height:226px;background:linear-gradient(160deg,#b7a077,#6b5a44)"></div>
<div class="dots blue" style="left:307px;top:3672px"><i></i><i class="on"></i><i></i><i></i></div>
<div class="sq" style="left:600px;top:3657px;width:42px"><svg width="8" height="12" viewBox="0 0 8 12"><path d="M7 1L2 6l5 5" fill="none" stroke="#fff" stroke-width="1.6"/></svg></div>
<div class="sq" style="left:652px;top:3657px;width:42px"><svg width="8" height="12" viewBox="0 0 8 12"><path d="M1 1l5 5-5 5" fill="none" stroke="#fff" stroke-width="1.6"/></svg></div>
<h2 class="abs serif team-title">Meet Our Team</h2>
<p class="abs team-text">Lorem ipsum dolor sit amet, consectetur adipiscing elit. Cras est magna, consectetur ut metus vel, porta posuere maurist. Curabitur congue risus sem, in gravida leo molestie quis. Duis hendrerit, enim id efficitur rutrum, ipsum sapien gravida est, non placerat mi purus a velit. Quisque rutrum diam in libero laoreet malesuada. Etiam tincidunt auctor leo sit amet varius. Pellentesque eu metus magna. Aliquam semper tempus massa, sit amet lobortis urna pharetra in. Morbi non diam et diam.</p>
<div class="btn btn-line" style="left:890px;top:3618px;width:188px;height:42px;font-size:14px;font-weight:700">Meet Entire Team</div>

<!-- footer -->
<footer class="abs footer">
  <div class="logo" style="left:122px;top:110px;color:#fff;font-size:22px">BRISKLUME<br>HOMES</div>
  <div class="abs" style="left:110px;top:201px"><i class="soc"></i><i class="soc"></i><i class="soc"></i><i class="soc"></i></div>
  <div class="fcol" style="left:384px;top:102px"><h4>Contact Us</h4>720-555-0148<br>hello@brisklumehomes.net<br><span style="line-height:16px;display:block;padding-top:7px">118, Marlow Ave Fort Collins,<br>CO 80521</span></div>
  <div class="fcol" style="left:618px;top:102px"><h4>Featured</h4>Houses<br>Lands<br>Commercial</div>
  <div class="fcol" style="left:803px;top:102px"><h4>Quick Links</h4>Home<br>Solutions<br>Gallery<br>Pricing</div>
  <div class="fcol" style="left:954px;top:132px">Our Team<br>Career Oppertunities<br>Demo<br>COVID-19 Protocols</div>
  <div class="abs" style="left:80px;top:300px;width:1040px;height:1px;background:#555"></div>
  <div class="abs" style="left:124px;top:314px;font-size:12px;color:#ccc">Copyright ©2020 brisklumehomes.net</div>
  <div class="abs" style="left:757px;top:314px;font-size:12px;color:#ccc;word-spacing:2px">Privacy policy &nbsp;&nbsp;&nbsp; Cancellation policy &nbsp;&nbsp;&nbsp; Terms and contidions</div>
</footer>
<div class="abs news">
  <div class="abs" style="left:90px;top:26px;color:#fff;font-size:21px;font-weight:700;line-height:32px">Get Latest And Greatest Offers.<br>Subscribe to our Newsletter!</div>
  <div class="abs" style="left:486px;top:35px;width:287px;height:33px;border:1px solid #fff;border-radius:4px;overflow:hidden;display:flex">
    <div style="width:180px;color:#dfe9f5;font-size:10px;padding:10px 14px">Please enter your email</div>
    <div style="flex:1;background:#fff;color:var(--brand);font-size:11px;font-weight:900;display:flex;align-items:center;justify-content:center">SUBSCRIBE</div>
  </div>
</div>

</body>
</html>
```